Nine Rung Ledger Remedy Seminar

I would like a flyer to hand out to participants at the speeches that we give. We are a CPA firm that specializes in entrepreneurs and realtors. We would like a flyer that looks crisp and clean, that integrates our logo and our company colors (shades of blue & gold). We would like the wording to be as laid out in the attached documents, but design is up to you. We would like a picture to go along with each point and are open to ideas. The flyer should be one page, preferably just the front.

Colors
3176b5
fee18a

Requirements
Must have
• Our logo and the wording supplied.
• A picture to go along with each topic.
Nice to have
• Images that pop, clean look, professional.
Should not have
• Look messy.

```html
<!DOCTYPE html>
<html lang="en">
<head>
<meta charset="utf-8">
<title>Nine Rung Ledger Remedy Seminar Agenda</title>
<link rel="stylesheet" href="https://fonts.googleapis.com/css2?family=Montserrat:wght@900&family=Arimo:wght@400;700&family=Libre+Baskerville:ital@1&display=swap">
<style>
  :root {
    --blue: #2462a9;
    --blue-title: #2c6fb2;
    --blue-soft: #5c8fcb;
    --gold: #f6d476;
    --gold-soft: #fbe7ad;
    --gold-line: #e8c75e;
    --ink: #3a3a3a;
    --body-ink: #404040;
    --paper: #f1f0ec;
    --number-grey: #7d7d7d;
  }
  * { box-sizing: border-box; margin: 0; padding: 0; }
  html, body { width: 923px; height: 1200px; overflow: hidden; }
  body {
    background: var(--paper);
    font-family: "Arimo", Arial, sans-serif;
    color: var(--body-ink);
    position: relative;
  }
  .backdrop {
    position: absolute; inset: 0;
    background: radial-gradient(ellipse at 60% 40%, #e3e6ea 0%, var(--paper) 70%);
  }
  .brand {
    position: absolute; left: 45px; top: 60px;
    font-family: "Montserrat", sans-serif; font-weight: 900;
    color: var(--blue); font-size: 34px; line-height: 34px;
    letter-spacing: -0.5px; display: flex; align-items: center; gap: 10px;
  }
  .brand-mark { width: 18px; height: 18px; background: var(--blue); }
  .brand small { display: block; font-size: 20px; line-height: 24px; }
  .tagline {
    position: absolute; right: 46px; top: 84px; text-align: right;
    font-family: "Libre Baskerville", serif; font-style: italic;
    color: var(--blue); font-size: 17px; line-height: 24px;
  }
  .header-rule { position: absolute; left: 45px; top: 126px; }
  .title {
    position: absolute; left: 45px; top: 178px;
    font-family: "Montserrat", sans-serif; font-weight: 900;
    font-size: 40px; line-height: 48px; letter-spacing: 0.3px;
    color: var(--ink); text-transform: uppercase;
  }
  .title .accent { color: var(--blue-title); display: block; }
  .step {
    position: absolute; width: 274px;
    padding: 22px 30px 0 26px;
    font-size: 16.5px; line-height: 20.6px;
  }
  .step .num {
    display: block; font-family: "Montserrat", sans-serif; font-weight: 900;
    font-size: 27px; line-height: 28px; margin-bottom: 18px;
  }
  .step-picture {
    position: absolute; top: 16px; right: 16px;
    width: 72px; height: 44px; border-radius: 4px;
  }
  .step--blue { background: var(--blue); color: #fff; }
  .step--blue .num { color: var(--gold); }
  .step--blue .step-picture { background: linear-gradient(135deg, var(--blue-soft), var(--gold-soft)); }
  .step--gold { background: var(--gold); color: var(--body-ink); }
  .step--gold .num { color: var(--number-grey); }
  .step--gold .step-picture { background: linear-gradient(135deg, var(--gold-soft), var(--blue-soft)); }
  .col-1 { left: 45px; } .col-2 { left: 325px; } .col-3 { left: 604px; }
  .row-1 { top: 294px; height: 290px; }
  .row-2 { top: 592px; height: 272px; }
  .row-3 { top: 872px; height: 272px; }
  .slogan {
    position: absolute; left: 352px; top: 882px;
    font-family: "Montserrat", sans-serif; font-weight: 900;
    font-size: 29px; line-height: 36px; color: var(--blue-title);
    text-transform: uppercase; letter-spacing: 0.5px;
  }
  .contact {
    position: absolute; left: 352px; top: 1014px;
    font-size: 15.5px; line-height: 19.5px; color: var(--body-ink);
    font-style: normal;
  }
  .contact p + p { margin-top: 18px; }
  .contact .web { font-weight: 700; color: #222; }
  .footer-rule {
    position: absolute; left: 45px; top: 1176px;
    width: 832px; height: 2px; background: var(--gold-line);
  }
</style>
</head>
<body>
  <div class="backdrop" role="img" aria-label="Soft blurred office backdrop with a faint growth chart"></div>

  <div class="brand"><span class="brand-mark"></span><span>Tallyrock<small>Advisors</small></span></div>
  <div class="tagline">A professional<br>Accounting Corporation</div>
  <svg class="header-rule" width="832" height="16" viewBox="0 0 832 16" aria-hidden="true">
    <line x1="0" y1="8" x2="832" y2="8" stroke="var(--gold-line)" stroke-width="2"/>
    <polygon points="577,1 593,8 577,15" fill="var(--gold-line)"/>
  </svg>

  <h1 class="title">Nine Rung Ledger Remedy<span class="accent">Seminar Agenda:</span></h1>

  <section class="step step--blue col-1 row-1"><span class="step-picture" role="img" aria-label="Photo of business owner reviewing S Corporation papers"></span><span class="num">1</span>We will first show you how to eliminate much of your self-employment tax on your return by converting your business into an S Corporation.&nbsp; A business owner making over $120,000 per year can save about $12,000 per year by doing this.</section>
  <section class="step step--gold col-2 row-1"><span class="step-picture" role="img" aria-label="Photo of a home hosting a board meeting"></span><span class="num">2</span>We will show you how to get tax free income from your corporation by renting you home to the corporation for the board meetings. Many of our clients are getting up to $21,000 in tax free income which could put $8,400 cash into your pocket.</section>
  <section class="step step--blue col-3 row-1"><span class="step-picture" role="img" aria-label="Photo of a phone snapping a receipt"></span><span class="num">3</span>We will show you the easiest way to track your expenses so that the only thing you will have to do to have rock solid books is to take a picture of the receipt and throw it away. It doesn’t get any better than that.</section>
  <section class="step step--gold col-1 row-2"><span class="step-picture" role="img" aria-label="Photo of a year-end planning calendar"></span><span class="num">4</span>Next, we show you the importance of tax planning and why it is critical to meet with your CPA before the end of the year and not just when you do your tax preparation.</section>
  <section class="step step--blue col-2 row-2"><span class="step-picture" role="img" aria-label="Photo of a family business workplace"></span><span class="num">5</span>We will show you how to hire your children and get $7,500 per child tax free. This will save you $3,000 per child in income tax reduction.</section>
  <section class="step step--gold col-3 row-2"><span class="step-picture" role="img" aria-label="Photo of a graduation cap on a stack of books"></span><span class="num">6</span>We will discuss how to make your child’s college education tax deductible. With college cost spiraling out of control this is a biggie.&nbsp; Most of our clients have a savings of about $12,000 per year of college.</section>
  <section class="step step--blue col-1 row-3"><span class="step-picture" role="img" aria-label="Photo of two office buildings side by side"></span><span class="num">7</span>Our grand finale is to show you how to use, not one, but two corporations to get a several hundred thousand dollar tax deferral, get an interest free loan from the government and use that money to grow your business and your wealth.</section>

  <p class="slogan">If they drive by with a<br>machine gun you don’t<br>have to stand up.</p>

  <address class="contact">
    <p>Tallyrock Advisors, A Professional Accounting Corporation<br>872 Orchard Row, Ste. B, Linden Vale, CA 95412<br>Phone: 555-014-2270 &nbsp;•&nbsp; Fax: 555-014-2271</p>
    <p>marlow@tallyrockadvisors.com<br>quinn@tallyrockadvisors.com<br><span class="web">www.tallyrockadvisors.com</span></p>
  </address>

  <div class="footer-rule" aria-hidden="true"></div>
</body>
</html>
```